We are a specialised ICT Consultancy firm based in Perth, Western Australia. We are looking for an A4 brochure titled “Building Tomorrow Together” that we can use. I have created the content we would like for the brochure in the attachment “Building Tomorrow Together.docx”.
We would like the following on the brochure:
• A copy of the Australian Flag (can be static or rippling in the wind).
• Our logo
• Must be the Avantgarde blue theme
I have included copies of similar brochures so the designer can get an idea of the theme we are looking for.

```html
<!DOCTYPE html>
<html lang="en">
<head>
<meta charset="utf-8">
<title>Building Tomorrow Together – Brochure</title>
<link rel="stylesheet" href="https://fonts.googleapis.com/css2?family=Roboto:wght@400;500;700&family=Roboto+Condensed:wght@400;700&display=swap">
<style>
:root{
  --stage:#7c9bc9;
  --paper:#eef0f2;
  --navy:#1d2a6e;
  --blue:#2f5fb8;
  --bright:#3f7fd6;
  --grey:#b8babd;
  --ink:#2b2d3a;
  --white:#ffffff;
}
*{margin:0;padding:0;box-sizing:border-box}
html,body{width:739px;height:1200px;overflow:hidden}
body{background:var(--stage);font-family:"Roboto",sans-serif;color:var(--ink);position:relative}
.spread{position:absolute;left:30px;width:680px;height:481px;display:flex;box-shadow:0 14px 30px rgba(20,35,80,.35)}
.spread--outer{top:70px}
.spread--inner{top:640px}
.page{position:relative;width:340px;height:481px;background:var(--paper);overflow:hidden}
.page + .page{box-shadow:inset 8px 0 10px -8px rgba(0,0,0,.18)}
.page svg.shapes{position:absolute;inset:0;width:340px;height:481px}
.abs{position:absolute}
.cond{font-family:"Roboto Condensed",sans-serif}

/* brand name */
.brand{font-family:"Roboto",sans-serif;font-weight:700;color:var(--navy);font-size:11px;letter-spacing:1.5px;display:flex;align-items:center;gap:5px;text-transform:uppercase}
.brand-dot{width:7px;height:7px;background:var(--navy)}

/* contact page */
.contact-title{left:42px;top:138px;font-size:22px;color:var(--navy);display:flex;align-items:center;gap:7px}
.label{font-family:"Roboto Condensed",sans-serif;font-weight:700;color:var(--navy);font-size:10px;text-transform:uppercase}
.contact-item{display:flex;gap:7px;align-items:flex-start;width:135px}
.contact-item svg{flex:none}
.contact-item strong{display:block;font-size:6.5px;color:var(--ink)}
.contact-item span{display:block;font-size:6px;line-height:1.35;color:#444}

/* cover */
.cover-title{left:20px;top:246px;color:var(--white);font-size:22px;line-height:1.05;text-transform:uppercase}
.cover-title .hl{display:inline-block;background:var(--navy);padding:1px 5px;border:1px solid rgba(255,255,255,.6)}
.cover-title b{font-weight:700}
.rule{height:1px;background:rgba(255,255,255,.55);width:130px;margin:8px 0 6px}
.cover-body{left:20px;top:330px;width:190px;font-size:7px;line-height:1.45;color:var(--white)}

/* inner */
.section-title{font-size:20px;line-height:1.05;color:var(--navy);text-transform:uppercase}
.section-title b{color:var(--blue);font-weight:700}
.body-text{font-size:7px;line-height:1.5;color:#3a3c48}
.commit-title{font-family:"Roboto Condensed",sans-serif;font-weight:700;font-size:8.5px;color:var(--blue);text-transform:uppercase}
.commit-list{list-style:none}
.commit-list li{display:flex;gap:8px;align-items:center;margin-bottom:9px}
.commit-list strong{display:block;font-size:6.5px;color:var(--ink)}
.commit-list span{display:block;font-size:6px;color:#444}
</style>
</head>
<body>

<!-- Outer spread: back cover + front cover -->
<section class="spread spread--outer">
  <article class="page page--contact">
    <svg class="shapes" viewBox="0 0 340 481">
      <defs>
        <linearGradient id="cityDusk" x1="0" y1="0" x2="0" y2="1">
          <stop offset="0" stop-color="#1c2a7a"/><stop offset="1" stop-color="#2d3f9a"/>
        </linearGradient>
      </defs>
      <polygon points="92,0 160,0 126,72" fill="var(--bright)"/>
      <polygon points="150,0 310,0 205,190" fill="url(#cityDusk)" role="img" aria-label="Night city skyline photograph"/>
      <polygon points="0,260 55,330 0,330" fill="var(--grey)" opacity=".5"/>
      <polygon points="0,400 340,455 340,481 0,481" fill="var(--navy)"/>
      <polygon points="0,430 200,481 0,481" fill="var(--blue)" opacity=".7"/>
    </svg>
    <h2 class="abs contact-title cond">
      <svg width="12" height="11" viewBox="0 0 12 11"><polygon points="0,0 12,0 6,11" fill="var(--blue)"/></svg>CONTACT US
    </h2>
    <p class="abs label" style="left:42px;top:172px">Address:</p>
    <div class="abs contact-item" style="left:42px;top:190px">
      <svg width="20" height="18" viewBox="0 0 20 18"><polygon points="10,0 20,18 0,18" fill="var(--navy)"/><circle cx="10" cy="12" r="2.3" fill="#fff"/></svg>
      <div><strong>Office:</strong><span>12/4 Harbourview Road, Lakeside, 6100 Australia</span></div>
    </div>
    <p class="abs label" style="left:42px;top:228px">Get in touch:</p>
    <div class="abs contact-item" style="left:42px;top:250px">
      <svg width="20" height="18" viewBox="0 0 20 18"><polygon points="10,0 20,18 0,18" fill="var(--navy)"/><path d="M8 9.5c.6 1.6 1.6 2.6 3 3.2l1-1 1.5.8-.6 1.4c-2.7-.2-5-2.6-5.3-5.4l1.4-.5.7 1.5z" fill="#fff"/></svg>
      <div><strong>Call Us:</strong><span>08 5550 1234</span></div>
    </div>
    <div class="abs contact-item" style="left:185px;top:250px">
      <svg width="20" height="18" viewBox="0 0 20 18"><polygon points="10,0 20,18 0,18" fill="var(--navy)"/><circle cx="10" cy="12" r="2.3" fill="#fff"/></svg>
      <div><strong>Postal:</strong><span>PO Box 210, Riverside Point WA 6150</span></div>
    </div>
    <div class="abs contact-item" style="left:42px;top:300px;width:145px">
      <svg width="20" height="18" viewBox="0 0 20 18"><polygon points="10,0 20,18 0,18" fill="var(--navy)"/><rect x="6.5" y="10" width="7" height="5" fill="#fff"/><path d="M6.5 10l3.5 2.6 3.5-2.6" stroke="var(--navy)" stroke-width=".7" fill="none"/></svg>
      <div><strong>Email Address:</strong><span>accounts@northlinetech.com.au</span></div>
    </div>
    <div class="abs contact-item" style="left:185px;top:300px;width:150px">
      <svg width="20" height="18" viewBox="0 0 20 18"><polygon points="10,0 20,18 0,18" fill="var(--navy)"/><rect x="6.5" y="10" width="7" height="5" fill="#fff"/><path d="M6.5 10l3.5 2.6 3.5-2.6" stroke="var(--navy)" stroke-width=".7" fill="none"/></svg>
      <div><strong>Email Address:</strong><span>sales@northlinetech.com.au</span></div>
    </div>
  </article>

  <article class="page page--cover">
    <svg class="shapes" viewBox="0 0 340 481">
      <defs>
        <linearGradient id="globeCity" x1="0" y1="0" x2="1" y2="1">
          <stop offset="0" stop-color="#6f8fc6"/><stop offset=".5" stop-color="#2c4d9a"/><stop offset="1" stop-color="#142160"/>
        </linearGradient>
        <linearGradient id="flagSky" x1="0" y1="0" x2="0" y2="1">
          <stop offset="0" stop-color="#4b86d6"/><stop offset="1" stop-color="#22307a"/>
        </linearGradient>
        <linearGradient id="navyPanel" x1="0" y1="0" x2="1" y2="1">
          <stop offset="0" stop-color="#2c4aa6"/><stop offset="1" stop-color="#1a2566"/>
        </linearGradient>
      </defs>
      <polygon points="0,245 340,205 340,481 0,481" fill="url(#navyPanel)"/>
      <polygon points="150,168 340,168 340,300 290,470" fill="url(#globeCity)" stroke="#fff" stroke-width="3" role="img" aria-label="Globe over a city skyline at night photograph"/>
      <polygon points="98,102 178,102 150,142" fill="var(--blue)"/>
      <polygon points="252,112 322,112 290,160" fill="var(--grey)"/>
      <polygon points="225,70 282,172 168,172" fill="url(#flagSky)" stroke="#fff" stroke-width="3" role="img" aria-label="Australian flag on a flagpole photograph"/>
    </svg>
    <div class="abs brand" style="left:188px;top:32px"><i class="brand-dot"></i>Northline</div>
    <h1 class="abs cover-title cond"><span class="hl">Building</span><br><b>Tomorrow</b> Together</h1>
    <div class="abs cover-body">
      <div class="rule"></div>
      As a 100% Western Australian-owned ICT provider, Northline Technologies delivers top-tier tech solutions with a commitment to ethical sourcing that puts Australia first. By partnering with Northline, you are keeping your investment local and supporting Australia's future.
    </div>
  </article>
</section>

<!-- Inner spread -->
<section class="spread spread--inner">
  <article class="page page--challenge">
    <svg class="shapes" viewBox="0 0 340 481">
      <defs>
        <linearGradient id="flagWave" x1="0" y1="0" x2="1" y2="1">
          <stop offset="0" stop-color="#1b2470"/><stop offset=".6" stop-color="#2a3790"/><stop offset="1" stop-color="#3b4fb0"/>
        </linearGradient>
        <radialGradient id="techGlobe" cx=".5" cy=".35" r=".7">
          <stop offset="0" stop-color="#f2b25a"/><stop offset=".25" stop-color="#2aa6e0"/><stop offset="1" stop-color="#0a1a40"/>
        </radialGradient>
      </defs>
      <polygon points="0,62 340,0 340,300 0,335" fill="url(#flagWave)" role="img" aria-label="Rippling Australian flag photograph"/>
      <polygon points="55,100 330,45 210,330" fill="url(#techGlobe)" stroke="#fff" stroke-width="4" role="img" aria-label="Hand touching a glowing digital world map photograph"/>
      <polygon points="190,40 255,32 232,80" fill="var(--grey)"/>
      <polygon points="130,292 168,245 178,292" fill="var(--blue)"/>
      <polygon points="270,255 320,240 300,290" fill="var(--blue)"/>
    </svg>
    <h2 class="abs section-title cond" style="left:30px;top:355px">The Challenge of<br>Big Tech <b>Tax Avoidance</b></h2>
    <p class="abs body-text" style="left:30px;top:405px;width:280px">
      Multinational IT corporations frequently minimise their Australian tax obligations by artificially inflating costs to local subsidiaries. This shifts profits offshore and drastically reduces domestic margins, allowing them to avoid paying their fair share of Australian tax. As a local provider, Northline ensures your ICT spending actively contributes to the Australian tax base and supports national growth.
    </p>
  </article>

  <article class="page page--advantage">
    <svg class="shapes" viewBox="0 0 340 481">
      <defs>
        <linearGradient id="towerView" x1="0" y1="0" x2="0" y2="1">
          <stop offset="0" stop-color="#1d3c8a"/><stop offset=".6" stop-color="#3a6bb5"/><stop offset="1" stop-color="#8fb0d6"/>
        </linearGradient>
      </defs>
      <polygon points="290,90 340,60 340,481 275,481" fill="url(#towerView)" role="img" aria-label="City tower and harbour aerial photograph"/>
      <polygon points="245,262 300,225 300,300" fill="var(--grey)"/>
    </svg>
    <div class="abs brand" style="left:120px;top:28px"><i class="brand-dot"></i>Northline</div>
    <h2 class="abs section-title cond" style="left:40px;top:55px;width:220px;text-align:center">The Locally<br><b>Sourced</b> Advantage</h2>
    <p class="abs body-text" style="left:40px;top:103px;width:220px;text-align:center">
      Northline is committed to a 100% Australian-owned supply chain. We ensure every dollar spent reinvests directly into our national economy—with all taxes paid straight to the Australian Taxation Office (ATO).
    </p>
    <div class="abs" style="left:40px;top:160px;width:215px;display:flex;gap:8px;align-items:flex-start">
      <svg width="24" height="22" viewBox="0 0 24 22"><polygon points="12,0 24,22 0,22" fill="var(--navy)"/></svg>
      <div>
        <p class="commit-title">Northline's Australian-First Commitment</p>
        <p class="body-text">At Northline, we endeavour to maintain an entirely local supply chain.</p>
      </div>
    </div>
    <ul class="abs commit-list" style="left:55px;top:210px;width:190px">
      <li><svg width="18" height="16" viewBox="0 0 18 16"><polygon points="9,0 18,16 0,16" fill="var(--navy)"/><circle cx="9" cy="11" r="2" fill="#fff"/></svg><div><strong>Distributors:</strong><span>Preferencing Australian-owned supply networks.</span></div></li>
      <li><svg width="18" height="16" viewBox="0 0 18 16"><polygon points="9,0 18,16 0,16" fill="var(--navy)"/><circle cx="9" cy="11" r="2" fill="#fff"/></svg><div><strong>Telecommunications:</strong><span>Partnering with local network and telco providers.</span></div></li>
      <li><svg width="18" height="16" viewBox="0 0 18 16"><polygon points="9,0 18,16 0,16" fill="var(--navy)"/><circle cx="9" cy="11" r="2" fill="#fff"/></svg><div><strong>Data Infrastructure:</strong><span>Hosting within Australian-owned data centres.</span></div></li>
      <li><svg width="18" height="16" viewBox="0 0 18 16"><polygon points="9,0 18,16 0,16" fill="var(--navy)"/><circle cx="9" cy="11" r="2" fill="#fff"/></svg><div><strong>Strategic Partners:</strong><span>Prioritising collaboration with domestic IT vendors.</span></div></li>
    </ul>
  </article>
</section>

</body>
</html>
```